High Tech Software Startup needs Letterhead Design

We need a letterhead for a startup company base in Brazil. The letterhead should combine with our logo attached here.
We are a team of professionals in Java for web and mobile with iOS and android development.
We are looking for a modern and futuristc design.

Target Market(s)

CIO, IT managers of mid to big size companies

Industry/Entity Type

It Company

```html
<!DOCTYPE html>
<html lang="en">
<head>
<meta charset="utf-8">
<title>Vantro Letterhead</title>
<link href="https://fonts.googleapis.com/css2?family=Allura&family=Montserrat:wght@400;500;700&display=swap" rel="stylesheet">
<style>
  :root {
    --backdrop: #2b2b2b;
    --paper: #f7f8f8;
    --paper-shade: #eceeef;
    --ink: #2a2a2a;
    --signature-ink: #1f2fc4;
    --brand-navy: #0f3a66;
    --brand-deep: #0a2d52;
    --brand-cyan: #2aa7e0;
    --footer-label: #3fb0e6;
    --footer-text: #ffffff;
  }
  * { margin: 0; padding: 0; box-sizing: border-box; }
  html, body { width: 1200px; height: 900px; overflow: hidden; }
  body {
    background: var(--backdrop);
    font-family: "Montserrat", sans-serif;
    position: relative;
  }
  .letterhead {
    position: absolute;
    left: 317px; top: 49px;
    width: 566px; height: 802px;
    background: linear-gradient(135deg, var(--paper) 0%, var(--paper-shade) 55%, var(--paper) 100%);
    overflow: hidden;
  }
  .brand {
    position: absolute; left: 41px; top: 42px;
    display: flex; align-items: center; gap: 7px;
    color: var(--brand-navy);
    font-weight: 700; font-size: 25px; letter-spacing: 0.5px; line-height: 1;
  }
  .brand__square { width: 26px; height: 26px; background: var(--brand-navy); }
  .letter-body {
    position: absolute; left: 81px; top: 268px; width: 405px;
    color: var(--ink);
    font-size: 9.8px; line-height: 12.5px;
    text-align: justify;
  }
  .letter-body p + p { margin-top: 12.5px; }
  .sign-off { position: absolute; left: 74px; top: 594px; }
  .signature {
    font-family: "Allura", cursive;
    font-size: 30px; line-height: 34px;
    color: var(--signature-ink);
  }
  .sign-off__role {
    margin-top: 1px; margin-left: 7px;
    font-size: 11px; color: var(--ink);
  }
  .footer-band { position: absolute; left: 0; top: 0; width: 566px; height: 802px; }
  .swoosh-area {
    position: absolute; right: 0; top: 595px;
    width: 300px; height: 160px;
    background: linear-gradient(160deg, rgba(15,58,102,0) 20%, rgba(15,58,102,0.85) 60%, var(--brand-navy) 100%);
    clip-path: polygon(100% 0, 100% 100%, 0 100%);
  }
  .contact-bar {
    position: absolute; left: 26px; top: 766px;
    display: flex; font-size: 6.6px; line-height: 8.6px; color: var(--footer-text);
  }
  .contact-bar__group {
    display: grid; grid-template-columns: auto auto; column-gap: 4px;
    padding-right: 7px; margin-right: 7px;
    border-right: 0.8px solid rgba(255,255,255,0.45);
  }
  .contact-bar__group:last-child { border-right: none; }
  .contact-bar__label { color: var(--footer-label); }
</style>
</head>
<body>
  <main class="letterhead">
    <svg class="footer-band" viewBox="0 0 566 802" aria-hidden="true">
      <defs>
        <linearGradient id="band-fill" x1="0" y1="0" x2="0" y2="1">
          <stop offset="0" stop-color="var(--brand-navy)"/>
          <stop offset="1" stop-color="var(--brand-deep)"/>
        </linearGradient>
      </defs>
      <path d="M0 724 C120 744 200 752 263 752 L566 752 L566 802 L0 802 Z" fill="url(#band-fill)"/>
    </svg>
    <div class="swoosh-area" role="img" aria-label="Decorative blue swoosh sweeping up the lower right corner"></div>

    <header class="brand">
      <span class="brand__square"></span>
      <span class="brand__name">VANTRO</span>
    </header>

    <section class="letter-body">
      <p>Letterhead samples are a great way of deciding what kind of letterhead you want to design for you and your company. The internet has a ton of great letterhead samples to browse through. Whether you want something simple, with just a couple lines of text of your business information, or something decorative and stunning, with photos and logos on the top and bottom of the page, it will be easy to find what you want, because there are samples online for basically any type of letterhead you could want.</p>
      <p>Any business could easily benefit from browsing through some letterhead samples, if only to get an idea for what kind of letterhead their company might want. Letterheads are just one of the tools that a business professional could use to help increase their customer base, and to really be memorable to everyone they write a letter to. Letterhead is quite an effective tool for marketing and advertising, but because it’s such a simple and well known idea, it is often unfairly overlooked. Make sure you don’t make that mistake, and make some letterhead samples of your own today.</p>
      <p>Whether you want to get new customers to remember you and become part of your clientele, or you just want to send out friendly reminders to your existing clients, customizing your own letterhead samples can really help you out. Try out some letterhead samples and you will not regret it, and I’m sure you will add a new tool to your business’ arsenal of networking, marketing, and advertising tools.</p>
    </section>

    <div class="sign-off">
      <p class="signature">Marcus Ellery</p>
      <p class="sign-off__role">company director</p>
    </div>

    <footer class="contact-bar">
      <div class="contact-bar__group">
        <span class="contact-bar__label">Phone</span><span>800 214 36 70</span>
        <span class="contact-bar__label">Cell</span><span>555 302 18 94</span>
      </div>
      <div class="contact-bar__group">
        <span class="contact-bar__label">Email</span><span>hello@vantro.com</span>
        <span class="contact-bar__label">Web</span><span>www.vantro.com</span>
      </div>
      <div class="contact-bar__group">
        <span>48 Harbor Lane</span><span></span>
        <span>Brookfield, New York 12345</span><span></span>
      </div>
    </footer>
  </main>
</body>
</html>
```